Stylish Website Design for Harbourline Plunge Works

Harbourline Plunge Works will be building a new website in a Wordpress CMS.
The design will be stylish, clean with strong powerful images that represent their work. Users scrolling pages will have call to actions listed at various intervals that drives traffic through the website journey.
The objective of the website journey is to direct clients to the ‘Instant Quote’. This will take visitors through an 8 Step calculator.
1. Capture Customer Details (Email and Full Name).
2. Pool Size
3. Shell Colour
4. Exterior Colour
5. Decking Option
6. Access Options
7. Selections (choosing the sanitisation and pump)
8. Extras
The instant quote will be visually appealing and engaging. The next button for each step will capture the data and identify the step the customer aborts.
Here is a link to the current calculator OLD QUOTE: https://harbourlineplungeworks.com.au/quote
The current design has the following issues that need to be resolved with the new design, please do not replicate the current look and feel. We are seeking a complete redesign of the website.
1. No scrolling to go to the next tap.
2. Improve the image layout
3. Selections and Extras needs to be like an eCommerce site with images, access to descriptions, specifications etc.
4. The steps need to feel like a journey
5. Gathering the customer’s name and email must be captured at the beginning
The aim is to keep the design simple but stylish. The navigation should have a search bar and clearly display the phone number as a link not an image, so it can be clicked on to make a call from a mobile device.
Please note the current website does not have the current logo, only a temporary one. Please use this one, the logo may be redesigned. https://files.brindlevault.example/share/7c21ae90d4f3b68e15a2c9077be4d1f3a6c8e2b5907d41fa3e6c82b1d95a0e47
IMAGES: Here are some of the company’s professional images. https://files.brindlevault.example/share/93e4b1d07a2c58f6e1d3b9a04c7f25e8a1b6d0c39f4e72a85b1c6d0e3f9a72b4
There must be call to actions as you scroll the page.
• Contact Us Button
• Download Brochure (name may be changed)
o This will capture a customers name and email to send a brochure
• Join Our Team
• Live Chat (Floats bottom right)
• Order Now Button
Site Map
• Home page – via logo
• Design and Build - http://harbourlineplungeworks.com.au/learn-more
o Instant Quote
o Packages
There may be 3 packages
o The Process
o Financing
• About Us
o Choosing Us
o Locations
o Careers
• Blogs
o Events
o Legends
• Gallery
• Contact Us
Footer
• Social Media icons
o TikTok
o Instagram
o Facebook
o Youtube
o Twitter
• Privacy Policy (Content on the current site but improve layout)
• Specifications
• Site Map
• Images of Certifications (as shown on the current site)
• Company Contact Details (Address on Phone)
• Marketing News Sign Up
Target Market(s)
Business to Consumer, Renovations
Industry/Entity Type
Construction and Renovations
Number of Pages Required
5+ page
Requirements
Must have
- Read the description but home page design and calculator design.
Nice to have
- Included in the description.

```html
<!DOCTYPE html>
<html lang="en">
<head>
<meta charset="utf-8">
<title>Harbourline Plunge Works</title>
<link href="https://fonts.googleapis.com/css2?family=Poppins:wght@300;400;500;600;700;800&display=swap" rel="stylesheet">
<style>
:root{
  --orange:#f7941d;
  --orange-dark:#e67e0c;
  --ink:#1f1f1f;
  --text:#555;
  --muted:#8a8a8a;
  --light:#f2f2f2;
  --footer:#262626;
  --white:#fff;
  --grey-card:#5b5b5b;
}
*{box-sizing:border-box;margin:0;padding:0}
html,body{width:1200px;height:4552px;overflow:hidden}
body{font-family:'Poppins',sans-serif;color:var(--text);background:var(--white);position:relative}
.abs{position:absolute}
a{color:inherit;text-decoration:none}

/* header */
.topbar{left:560px;top:0;width:640px;height:34px;background:var(--orange);border-bottom-left-radius:20px;display:flex;align-items:center;gap:34px;padding-left:60px;color:var(--white);font-size:12px;font-weight:500}
.topbar span{display:flex;align-items:center;gap:6px}
.brand{left:40px;top:14px;display:flex;align-items:center;gap:10px;z-index:3}
.brand-dot{width:30px;height:30px;border-radius:50%;background:var(--orange)}
.brand-name{font-weight:700;font-size:19px;color:var(--white);line-height:1.1;width:200px}
.nav{left:570px;top:52px;display:flex;gap:26px;align-items:center;font-size:13px;font-weight:500;color:var(--white);z-index:3}
.nav .active{color:var(--orange)}
.nav .btn-outline{border:1.5px solid var(--white);padding:6px 14px;border-radius:3px}

/* hero */
.hero{left:0;top:0;width:1200px;height:860px;background:linear-gradient(180deg,#a9c3cf 0%,#8aa8a4 30%,#55704c 62%,#3e5236 100%)}
.hero-shade{left:0;top:0;width:1200px;height:860px;background:linear-gradient(90deg,rgba(0,0,0,.45),rgba(0,0,0,0) 60%)}
.hero h1{left:88px;top:308px;width:560px;font-size:50px;line-height:1.1;font-weight:800;color:var(--white);text-transform:uppercase}
.hero p{left:88px;top:470px;width:560px;font-size:15px;line-height:1.6;color:var(--white)}
.btn{display:inline-block;background:var(--orange);color:var(--white);font-size:12px;font-weight:600;text-transform:uppercase;padding:10px 22px;border-radius:3px}
.hero .btn{position:absolute;left:88px;top:530px}
.pager{left:1140px;top:300px;color:var(--white);font-size:12px;font-weight:600;display:flex;flex-direction:column;gap:14px}
.pager span:first-child{color:var(--orange)}
.wave{left:0;width:1200px}

/* about */
.about-photo{left:84px;top:712px;width:440px;height:440px;border-radius:50%;background:linear-gradient(160deg,#3c6f8a,#6c8f7a 55%,#a8987a);border:10px solid var(--white);box-shadow:0 0 0 6px var(--orange)}
.eyebrow{font-size:13px;font-weight:600;color:var(--orange);text-transform:uppercase}
.h2{font-size:42px;font-weight:700;color:var(--ink);line-height:1.15}
.about-text{left:598px;top:836px;width:520px}
.about-text .h2{margin:6px 0 16px}
.about-text p{font-size:14px;line-height:1.75;margin-bottom:18px}
.btn-dark{display:inline-block;border:1.5px solid var(--ink);color:var(--ink);font-size:11px;font-weight:600;padding:7px 14px;text-transform:uppercase}

/* sustainable */
.center{left:0;width:1200px;text-align:center}
.section-sub{font-size:14px;line-height:1.6;color:var(--text)}
.features{left:88px;top:1384px;width:1024px;display:flex;gap:8px}
.feature{flex:1;text-align:center}
.feature .img{height:316px}
.feature h4{margin-top:14px;font-size:15px;font-weight:500;color:var(--ink);letter-spacing:1px}
.arrow-btn{width:36px;height:36px;border-radius:50%;background:var(--orange);display:flex;align-items:center;justify-content:center}

/* cards */
.promo{top:1828px;width:504px;height:324px;border-radius:6px;display:flex;flex-direction:column;justify-content:center;align-items:center;text-align:center;color:var(--white);padding:0 60px}
.promo h3{font-size:28px;font-weight:600;margin-bottom:10px}
.promo p{font-size:13px;line-height:1.6}
.promo-orange{left:88px;background:linear-gradient(135deg,rgba(247,148,29,.95),rgba(230,126,12,.92)),#b9753a}
.promo-grey{left:608px;background:linear-gradient(135deg,rgba(80,80,80,.92),rgba(40,40,40,.9))}

/* heroism */
.hero-card{top:2332px;width:520px;height:328px;display:flex}
.hero-card .img{width:184px;height:100%}
.hero-card .body{flex:1;background:var(--white);box-shadow:0 6px 24px rgba(0,0,0,.08);padding:60px 28px}
.hero-card h4{font-size:16px;font-weight:600;color:var(--ink);line-height:1.4;margin-bottom:10px}
.hero-card p{font-size:12px;line-height:1.7}

/* gallery */
.gallery-bg{left:0;top:2720px;width:1200px;height:600px;background:var(--light)}
.gallery{left:0;top:2948px;width:1200px;height:284px;display:flex}
.gallery .img{flex:1;height:100%;position:relative}
.gallery-over{position:absolute;inset:0;background:rgba(247,148,29,.85);display:flex;justify-content:center;align-items:center;gap:10px}
.icon-circle{width:34px;height:34px;border-radius:50%;background:var(--white);display:flex;align-items:center;justify-content:center}

/* blog */
.blog{left:132px;top:3300px;width:560px}
.blog .h2{font-size:40px}
.blog > p{font-size:13px;line-height:1.6;width:440px;margin-top:6px}
.post{display:flex;gap:20px;margin-top:34px}
.post .img{width:140px;height:110px;flex:none}
.post h5{font-size:17px;font-weight:600;color:var(--ink)}
.post p{font-size:12px;line-height:1.6;margin:4px 0 10px}
.post small{font-size:11px;color:var(--muted)}
.polaroid{background:var(--white);padding:12px 12px 40px;box-shadow:0 8px 28px rgba(0,0,0,.18)}

/* brochure */
.brochure{left:88px;top:3812px;width:1052px;height:100px;background:var(--orange);border-radius:50px 0 0 50px;display:flex;align-items:center;padding:0 30px 0 48px;color:var(--white);z-index:2}
.brochure h3{font-size:24px;font-weight:600}
.brochure p{font-size:12px}
.field{width:200px;height:34px;border-radius:17px;background:var(--white);color:var(--muted);font-size:12px;padding:0 16px;display:flex;align-items:center}
.submit{height:34px;border-radius:17px;background:var(--ink);color:var(--white);font-size:12px;font-weight:600;padding:0 26px;display:flex;align-items:center}

/* footer */
.footer{left:0;top:3900px;width:1200px;height:652px;background:var(--footer)}
.foot-brand{left:88px;top:4120px;display:flex;align-items:center;gap:10px}
.foot-col{top:4150px;color:#cfcfcf;font-size:12px;line-height:2}
.foot-col h4{color:var(--white);font-size:20px;font-weight:600;margin-bottom:8px}
.foot-col li{list-style:none;display:flex;align-items:center;gap:8px}
.socials{left:820px;top:4284px;display:flex;gap:12px}
.socials span{width:30px;height:30px;border-radius:50%;border:1.5px solid #8c8c8c}
.bottom-bar{left:88px;top:4494px;width:1024px;display:flex;justify-content:space-between;font-size:12px;color:#bdbdbd}
.bottom-bar nav{display:flex;gap:36px}
.chat{left:1130px;top:4496px;width:46px;height:46px;border-radius:50%;background:var(--orange);display:flex;align-items:center;justify-content:center}
</style>
</head>
<body>

<!-- hero -->
<div class="abs hero" role="img" aria-label="Photo of a coastal home with a container plunge pool among green dunes"></div>
<div class="abs hero-shade"></div>

<div class="abs topbar">
  <span><svg width="12" height="12" viewBox="0 0 24 24" fill="#fff"><path d="M6.6 10.8a15 15 0 006.6 6.6l2.2-2.2a1 1 0 011-.25 11.4 11.4 0 003.6.6 1 1 0 011 1V20a1 1 0 01-1 1A17 17 0 013 4a1 1 0 011-1h3.5a1 1 0 011 1c0 1.25.2 2.45.6 3.6a1 1 0 01-.25 1z"/></svg><a href="tel:+61400218374">+61 400 218 374</a></span>
  <span>Mon–Fri 8am–5pm</span>
  <span>Portside, NSW</span>
  <span>DOWNLOAD BROCHURE</span>
</div>

<div class="abs brand"><span class="brand-dot"></span><span class="brand-name">Harbourline Plunge Works</span></div>

<nav class="abs nav">
  <a class="active" href="#">HOME</a>
  <a href="http://harbourlineplungeworks.com.au/learn-more">DESIGN &amp; BUILD</a>
  <a href="#">ABOUT US</a>
  <a href="#">BLOG</a>
  <a href="#">GALLERY</a>
  <a class="btn-outline" href="#">CONTACT US</a>
</nav>

<h1 class="abs" style="left:88px;top:308px;width:560px;font-size:50px;line-height:1.1;font-weight:800;color:#fff">WHY CHOOSE A SHIPPING CONTAINER POOL?</h1>
<p class="abs" style="left:88px;top:472px;width:560px;font-size:15px;line-height:1.6;color:#fff">Using the latest in technology we are able to create a lightweight product that can easily be transported.</p>
<a class="abs btn" style="left:88px;top:530px" href="https://harbourlineplungeworks.com.au/quote">Custom Quote</a>

<div class="abs pager"><span>01</span><span>02</span><span>03</span></div>

<svg class="abs wave" style="top:740px" width="1200" height="130" viewBox="0 0 1200 130" preserveAspectRatio="none">
  <path d="M0 70 C300 10 600 120 900 60 C1020 36 1120 40 1200 60 L1200 130 L0 130Z" fill="#fff"/>
</svg>

<!-- about -->
<div class="abs about-photo" role="img" aria-label="Photo of a swimmer diving into a container pool"></div>
<svg class="abs" style="left:60px;top:688px" width="490" height="490" viewBox="0 0 490 490"><path d="M60 380 A220 220 0 0 1 245 25" stroke="#f7941d" stroke-width="8" fill="none" stroke-linecap="round"/></svg>
<div class="abs about-text">
  <div class="eyebrow">About Us</div>
  <div class="h2">Any Home &amp; Any Site</div>
  <p>Previously pools were limited by the landscape of the property and requirement to excavate. With the Harbourline Plunge Works design you can place a pool where you never could. A flexible and intuitive design with technical structural support makes your new pool installation only limited by your imagination!</p>
  <a class="btn-dark" href="#">Read More</a>
</div>

<!-- sustainable -->
<div class="abs center" style="top:1252px"><div class="h2" style="font-size:40px">Sustainable</div></div>
<div class="abs center" style="top:1314px"><p class="section-sub" style="width:860px;margin:0 auto">Each Harbourline Plunge Works pool is assembled in a controlled factory in Australia making it the most sustainable pool on the market, reducing stress and our environmental footprint.</p></div>

<div class="abs features">
  <div class="feature"><div class="img" role="img" aria-label="Photo of pool filtration equipment" style="background:linear-gradient(160deg,#cfd3d6,#6d7378)"></div><h4>SMART</h4></div>
  <div class="feature"><div class="img" role="img" aria-label="Photo of a blue container pool with safety cover" style="background:linear-gradient(160deg,#3e8fd0,#1d5c94 60%,#8a8f94)"></div><h4>SAFE</h4></div>
  <div class="feature"><div class="img" role="img" aria-label="Photo of a child playing in a pool ring" style="background:linear-gradient(160deg,#5fc3e8,#f0c24a 60%,#3aa5d4)"></div><h4>PLAY</h4></div>
  <div class="feature"><div class="img" role="img" aria-label="Photo of a pool control touch panel" style="background:linear-gradient(160deg,#d9c6b0,#7e6a58)"></div><h4>TOUCH</h4></div>
</div>
<div class="abs arrow-btn" style="left:70px;top:1524px"><svg width="14" height="14" viewBox="0 0 24 24"><path d="M15 5l-7 7 7 7" stroke="#fff" stroke-width="3" fill="none"/></svg></div>
<div class="abs arrow-btn" style="left:1094px;top:1524px"><svg width="14" height="14" viewBox="0 0 24 24"><path d="M9 5l7 7-7 7" stroke="#fff" stroke-width="3" fill="none"/></svg></div>

<!-- promo cards -->
<svg class="abs" style="left:0;top:1740px" width="1200" height="540" viewBox="0 0 1200 540" preserveAspectRatio="none">
  <path d="M0 60 C300 0 700 100 1200 30 L1200 500 C800 540 400 470 0 520Z" fill="#f2f2f2"/>
</svg>
<div class="abs promo promo-orange" role="img" aria-label="Container pool being lifted by crane">
  <h3>Logistic Dream</h3>
  <p>Using the latest in technology we are able to create a light weight product that can easily be transported.</p>
</div>
<div class="abs promo promo-grey" role="img" aria-label="Container pool installed beside a home">
  <h3>Any Home &amp; Any Site</h3>
  <p>Previously pools were limited by the landscape of the property and requirement to excavate.</p>
</div>

<!-- heroism -->
<div class="abs center" style="top:2232px"><div class="h2" style="font-size:40px">Supporting Heroism</div></div>
<div class="abs hero-card" style="left:88px">
  <div class="img" role="img" aria-label="Portrait of a gold medal swimmer" style="background:linear-gradient(160deg,#c9a27e,#6b5644)"></div>
  <div class="body">
    <h4>Reid Calloway –100m Freestyle Gold Medalist</h4>
    <p>Supporting the living legend with a custom dual-wall pit in partnership with Harbourline during his training for the 2021 Games where he brought home a Silver Medal for the 100M freestyle.</p>
  </div>
</div>
<div class="abs hero-card" style="left:600px">
  <div class="img" role="img" aria-label="Portrait of a fitness athlete" style="background:linear-gradient(160deg,#bfa48c,#5d4e42)"></div>
  <div class="body">
    <h4>Tessa Marlowe – Functional Fitness Super Athlete</h4>
    <p>Dating back from her Harbourline rebuild, our relations with a magnet ice bath pool and a custom sauna pit.</p>
  </div>
</div>

<!-- gallery -->
<div class="abs gallery-bg"></div>
<svg class="abs" style="left:0;top:2690px" width="1200" height="80" viewBox="0 0 1200 80" preserveAspectRatio="none"><path d="M0 40 C400 0 800 80 1200 30 L1200 0 L0 0Z" fill="#fff"/></svg>
<div class="abs center" style="top:2874px"><div class="h2" style="font-size:40px">Our Gallery</div></div>
<div class="abs gallery">
  <div class="img" role="img" aria-label="Photo of container pool with timber deck under blue sky" style="background:linear-gradient(170deg,#5b8fc9,#3a5a3c)"></div>
  <div class="img" role="img" aria-label="Photo of backyard container pool in garden" style="background:linear-gradient(170deg,#7aa08a,#2f5160)"></div>
  <div class="img" role="img" aria-label="Photo of container pool by a house">
    <div class="gallery-over">
      <span class="icon-circle"><svg width="14" height="14" viewBox="0 0 24 24"><path d="M10 14a4 4 0 005.6 0l3-3a4 4 0 00-5.6-5.6l-1 1M14 10a4 4 0 00-5.6 0l-3 3a4 4 0 005.6 5.6l1-1" stroke="#f7941d" stroke-width="2.4" fill="none"/></svg></span>
      <span class="icon-circle"><svg width="14" height="14" viewBox="0 0 24 24"><circle cx="10" cy="10" r="6" stroke="#f7941d" stroke-width="2.4" fill="none"/><path d="M15 15l5 5" stroke="#f7941d" stroke-width="2.4"/></svg></span>
    </div>
  </div>
  <div class="img" role="img" aria-label="Photo of a container pool lifted at dusk" style="background:linear-gradient(170deg,#3f6fb0,#1e2f4a)"></div>
</div>

<!-- blog -->
<div class="abs blog">
  <div class="h2">Latest Blog</div>
  <p>Etiam rhoncus. Maecenas tempus, tellus eget condimentum rhoncus, sem quam semper libero, sit amet.</p>
  <div class="post">
    <div class="img" role="img" aria-label="Photo of a container pool with deck" style="background:linear-gradient(160deg,#8fb0c8,#44604f)"></div>
    <div><h5>Blog heading here</h5><p>Etiam rhoncus. Maecenas tempus, tellus eget condimentum rhoncus, sem quam.</p><small>September 7, 2021 &nbsp;|&nbsp; 1 Comment</small></div>
  </div>
  <div class="post">
    <div class="img" role="img" aria-label="Photo of a container pool being delivered" style="background:linear-gradient(160deg,#6d8fb5,#2f3d4d)"></div>
    <div><h5>Blog heading here</h5><p>Etiam rhoncus. Maecenas tempus, tellus eget condimentum rhoncus, sem quam.</p><small>September 7, 2021 &nbsp;|&nbsp; 1 Comment</small></div>
  </div>
</div>
<div class="abs polaroid" style="left:720px;top:3380px;width:270px;transform:rotate(8deg)"><div role="img" aria-label="Photo of a pool beside a home" style="height:210px;background:linear-gradient(160deg,#5fb3d6,#3b6b52)"></div></div>
<div class="abs polaroid" style="left:690px;top:3360px;width:270px;transform:rotate(-6deg)"><div role="img" aria-label="Photo of a blue container pool on a deck" style="height:210px;background:linear-gradient(160deg,#3fa8d8,#2b6b8f 55%,#8b6a4c)"></div></div>

<!-- footer -->
<div class="abs footer"></div>
<svg class="abs" style="left:0;top:3880px" width="1200" height="90" viewBox="0 0 1200 90" preserveAspectRatio="none"><path d="M0 20 L0 60 C400 10 800 90 1200 40 L1200 0 L0 0Z" fill="#fff"/></svg>

<div class="abs brochure">
  <div style="flex:1"><h3>Download Brochure</h3><p>Customers name and email to send a brochure</p></div>
  <div style="display:flex;gap:12px">
    <span class="field">Name</span><span class="field">Email</span><span class="submit">SUBMIT</span>
  </div>
</div>

<div class="abs foot-brand"><span class="brand-dot"></span><span class="brand-name" style="width:180px">Harbourline Plunge Works</span></div>

<div class="abs foot-col" style="left:328px">
  <h4>Useful Links</h4>
  <ul><li>Home</li><li>Design &amp; Build</li><li>About Us</li><li>Blog</li><li>Gallery</li><li>Contact Us</li></ul>
</div>
<div class="abs foot-col" style="left:572px">
  <h4>Contact Us</h4>
  <ul>
    <li><svg width="12" height="12" viewBox="0 0 24 24" fill="#f7941d"><path d="M12 2a7 7 0 00-7 7c0 5 7 13 7 13s7-8 7-13a7 7 0 00-7-7zm0 9.5A2.5 2.5 0 1112 6a2.5 2.5 0 010 5.5z"/></svg>14 Wharf Lane, Portside</li>
    <li><svg width="12" height="12" viewBox="0 0 24 24" fill="#f7941d"><path d="M3 5h18v14H3z M3 5l9 7 9-7" stroke="#262626" stroke-width="1.5"/></svg>hello@harbourlineplungeworks.com.au</li>
    <li><svg width="12" height="12" viewBox="0 0 24 24" fill="#f7941d"><path d="M6.6 10.8a15 15 0 006.6 6.6l2.2-2.2a1 1 0 011-.25 11.4 11.4 0 003.6.6 1 1 0 011 1V20a1 1 0 01-1 1A17 17 0 013 4a1 1 0 011-1h3.5a1 1 0 011 1c0 1.25.2 2.45.6 3.6a1 1 0 01-.25 1z"/></svg><a href="tel:+61400218374">+61 400 218 374</a></li>
    <li><svg width="12" height="12" viewBox="0 0 24 24"><circle cx="12" cy="12" r="9" stroke="#f7941d" stroke-width="2.5" fill="none"/></svg>harbourlineplungeworks.com.au</li>
  </ul>
</div>
<div class="abs socials" aria-label="Social media links"><span></span><span></span><span></span><span></span><span></span></div>

<div class="abs bottom-bar">
  <span>©Copyright 2021 | All Rights Reserved</span>
  <nav><span>Privacy policy</span><span>Specs</span><span>Support</span></nav>
</div>
<div class="abs chat" aria-label="Live chat"><svg width="20" height="20" viewBox="0 0 24 24" fill="#fff"><path d="M4 4h16v11H9l-5 4z"/></svg></div>

</body>
</html>
```